Wachsen statt schwinden - Flyer-Design für einen bahnbrechenden Workshop
Zielgruppe
Wir sind die Exzellenz in Faciliation - wir bringen Menschen so zusammen, dass etwas vollkommen Neues entsteht. Und wir bilden Menschen in dieser Kunst aus.
Aufgabenstellung
Mit unserem Workshop „Klar gestalten!“ begehen wir Neuland, für uns wie für unsere Kunden. Das wollen wir mit einem Flyer-Layout zum Ausdruck bringen.
Das Layout soll die bestehende KERO-CI weiterentwickeln. Insbesondere verzichten wir auf den im bisherigen CI abgelegten Bilder. Veränderbar sind sowohl Schriftarten als auch Layout-Elemente
Das Layout sollte generisch sein und die Grundlage für weitere Veranstaltungsflyer sein.
Uns schwebt ein reduziertes, konzentriertes Layout vor, bei dem der Inhalt wirken kann.
Zur Orientierung liegt der aktuelle Entwurf für unsere Homepage bei.
Die im Text angegebenen Inhalte müssen nicht alle im Flyer abgebildet werden. Der Designer/die Designerin kann eine Auswahl treffen der Inhalte, die sie für wichtig hält.
Zentral aber sind: Einführungspreis, Ort und Termin
Der Flyer ist ausschließlich zur digitalen Verteilung vorgesehen.

```html
<!DOCTYPE html>
<html lang="de">
<head>
<meta charset="utf-8">
<title>Wachsen statt schwinden – Workshop-Flyer</title>
<link href="https://fonts.googleapis.com/css2?family=Ubuntu:wght@300;400;500;700&display=swap" rel="stylesheet">
<style>
:root{
  --red:#ef4044;
  --wine:#6b2632;
  --stage:#6d6d6d;
  --paper:#ffffff;
  --ink:#5a5a5a;
  --ink-soft:#7a7a7a;
  --rule:#9a9a9a;
  --tint-a:#fde3e3;
  --tint-b:#f8c9cb;
}
*{box-sizing:border-box;margin:0;padding:0}
html,body{width:1200px;height:900px;overflow:hidden;background:var(--stage);font-family:"Ubuntu",sans-serif}
.canvas{position:relative;width:1200px;height:900px}
.page{position:absolute;top:76px;width:528px;height:748px;background:var(--paper);border-top:6px solid var(--red);border-bottom:8px solid var(--wine);overflow:hidden}
.page--front{left:56px}
.page--back{left:618px}
.page-label{position:absolute;top:846px;color:#fff;font-size:12px;font-weight:400}
.abs{position:absolute}
.brand-tile{position:absolute;top:0;right:41px;width:83px;height:78px;background:var(--red);display:flex;align-items:center;justify-content:center;color:#fff;font-weight:700;font-size:18px;letter-spacing:1px}
.bracket{position:absolute;width:19px;height:19px;border-color:var(--red);border-style:solid}
.bracket--tl{left:62px;top:60px;border-width:4px 0 0 4px}
.bracket--br{left:418px;top:428px;border-width:0 4px 4px 0}
.title-kicker{left:90px;top:72px;font-size:31px;font-weight:700;color:var(--red)}
.title-main{left:88px;top:104px;font-size:62px;font-weight:700;color:var(--red);letter-spacing:-0.5px}
.title-sub{left:90px;top:168px;font-size:36px;font-weight:700;color:var(--red)}
.dates{left:96px;top:220px;display:flex}
.date{font-size:19px;font-weight:500;color:var(--red);line-height:1.1}
.date small{display:block;font-size:15px;font-weight:500;margin-top:4px}
.date--left{text-align:right;padding-right:10px;border-right:1px solid var(--red);width:122px}
.date--right{padding-left:10px}
.dash-rule{left:93px;top:281px;width:337px;border-top:1px dashed var(--rule)}
.claim{left:93px;top:294px;font-size:17px;font-weight:500;color:var(--wine)}
.claim-sub{left:93px;top:318px;font-size:11px;font-weight:700;color:var(--wine)}
.body-copy{left:93px;width:336px;font-size:9.4px;font-weight:300;color:var(--ink);line-height:1.3}
.topics-head{left:92px;top:454px;font-size:10px;font-weight:500;color:var(--wine)}
.checklist{list-style:none}
.checklist li{position:relative;padding-left:12px;color:var(--ink);font-weight:300}
.checklist li::before{content:"";position:absolute;left:0;width:6px;height:6px;border:1px solid var(--wine);border-radius:1px}
.checklist li::after{content:"";position:absolute;left:1.8px;width:2px;height:3.5px;border:solid var(--wine);border-width:0 1px 1px 0;transform:rotate(40deg)}
.topics{left:93px;top:476px;width:340px}
.topics li{font-size:9.2px;line-height:16px}
.topics li::before{top:4px}
.topics li::after{top:4.6px}
.signup{left:75px;top:601px;font-size:9.5px;color:var(--wine)}
.signup-head{font-weight:400;margin-bottom:8px}
.signup-line{display:flex;align-items:center;gap:6px;font-weight:300;color:var(--ink);margin-bottom:4px}
.signup-line svg{width:9px;height:9px}
.signup-org{margin-top:9px;line-height:1.45;color:var(--wine)}
.signup-org b{font-weight:500}
.price{left:234px;top:614px;width:218px;height:77px;display:flex;border:1px solid var(--wine)}
.price-early{width:110px;background:var(--wine);color:#fff;padding:5px 0 0 11px}
.price-early .lbl{font-size:7.5px;font-weight:500}
.price-early .until{font-size:7.5px;margin-top:2px}
.price-early .until b{font-size:10px}
.price-early .amount{font-size:33px;font-weight:400;line-height:1;margin-top:2px}
.price-early .vat{font-size:6.5px;margin-top:1px}
.price-intro{flex:1;color:var(--wine);text-align:center;padding-top:17px}
.price-intro .lbl{font-size:7.5px;font-weight:500}
.price-intro .amount{font-size:35px;line-height:1;margin-top:3px}
/* back page */
.schedule-title{left:43px;top:44px;font-size:15.5px;font-weight:500;color:var(--red)}
.day-head{display:flex;align-items:center;gap:6px;font-size:11.5px;font-weight:500;color:var(--wine)}
.day-head::after{content:"";flex:1;border-top:1px solid var(--wine);margin-left:4px}
.day-head svg{width:14px;height:13px}
.day-copy{font-size:6.8px;font-weight:300;color:var(--ink-soft);line-height:1.45}
.day-list li{font-size:6.8px;line-height:13.6px}
.day-list li::before{top:3.6px}
.day-list li::after{top:4.2px}
.diagram-area{position:absolute;border-radius:50%;background:radial-gradient(circle,var(--tint-a) 0%,var(--tint-b) 100%)}
.diagram-area--steps{left:316px;top:140px;width:150px;height:150px}
.diagram-area--dims{left:325px;top:383px;width:130px;height:130px}
.diagram-title{position:absolute;text-align:center;color:var(--red);font-weight:500}
.diagram-title--steps{left:316px;top:199px;width:150px;font-size:11px;line-height:1.2}
.diagram-title--dims{left:300px;top:346px;width:180px;font-size:9.2px;line-height:1.3}
.trainer-head{left:300px;top:544px;width:180px;text-align:center;font-size:9.5px;font-weight:500;color:#333}
.trainer-photo{position:absolute;left:351px;top:562px;width:78px;height:78px;border-radius:50%;border:3px solid var(--wine);background:radial-gradient(circle at 50% 40%,#c9b8a8,#7d6b5f 70%,#4a4a4a)}
.trainer-name{left:280px;top:652px;width:220px;text-align:center;color:var(--wine)}
.trainer-name strong{display:block;font-size:11.5px;font-weight:500}
.trainer-name span{display:block;font-size:8.5px;font-weight:300}
.trainer-name em{display:block;font-style:normal;font-size:6.5px;font-weight:300;margin-top:2px}
</style>
</head>
<body>
<div class="canvas">

  <section class="page page--front">
    <div class="brand-tile">KERO</div>
    <span class="bracket bracket--tl"></span>
    <div class="abs title-kicker">Der Workshop</div>
    <div class="abs title-main">Wachsen</div>
    <div class="abs title-sub">statt schwinden</div>
    <div class="abs dates">
      <div class="date date--left">20-22 Sept.<small>in München</small></div>
      <div class="date date--right">11-13 Okt.<small>in Köln</small></div>
    </div>
    <div class="abs dash-rule"></div>
    <h2 class="abs claim">Wirksam werden! Klar gestalten!</h2>
    <div class="abs claim-sub">Das Prinzip von „Wachsen statt schwinden“</div>
    <p class="abs body-copy" style="top:347px">Wie du Teil der großen Wende wirst und andere Menschen in ihre transformative Kraft begleitest.</p>
    <p class="abs body-copy" style="top:383px">Der Workshop „Wachsen statt schwinden“ stellt dir dafür den notwendigen Rahmen zur Verfügung. Er spannt den Bogen vom „Was“ (sollen wir tun?) zum „Wie“ (sollen wir handeln?) und bietet ein reiches Spektrum an Methoden und Ansätzen, um Menschen in ihre transformative Kraft zu bringen.</p>
    <span class="bracket bracket--br"></span>
    <div class="abs topics-head">Der Workshop beinhaltet unter anderem folgende Themen:</div>
    <ul class="abs checklist topics">
      <li>Warum wir mehr als nachhaltig sein können und müssen</li>
      <li>Die sieben Schritte zur Wirksamkeit</li>
      <li>Die vier Dimensionen des Erneuerns</li>
      <li>Den Anfang im Ende erkennen: Wir wir Projekte gut aufsetzen</li>
      <li>Räume des Wandels schaffen</li>
      <li>Körperübungen und Methoden zur Arbeit mit Blockaden, zur Zielklärung und zur Entscheidungsfindung</li>
    </ul>
    <div class="abs signup">
      <div class="signup-head">Anmeldung:</div>
      <div class="signup-line"><svg viewBox="0 0 10 10"><rect x="0" y="0" width="10" height="10" rx="1.5" fill="var(--wine)"/><path d="M2 3.2h6v4H2z M2 3.2l3 2.2 3-2.2" fill="none" stroke="#fff" stroke-width="0.8"/></svg>kontakt@kero-werkstatt.de</div>
      <div class="signup-line"><svg viewBox="0 0 10 10"><rect x="0" y="0" width="10" height="10" rx="1.5" fill="var(--wine)"/><path d="M3 2.2c-.8.4-1 1.3-.4 2.6.7 1.5 1.8 2.6 3 3 .8.3 1.5 0 1.8-.6L6.3 6.1 5.5 6.6C4.7 6.2 4 5.4 3.6 4.6l.6-.7z" fill="#fff"/></svg>08141/5520384</div>
      <div class="signup-org"><b>KERO - Tun was ansteht</b><br>Ahornweg 5<br>85244 Röhrmoos</div>
    </div>
    <div class="abs price">
      <div class="price-early">
        <div class="lbl">für Fruhbucher :</div>
        <div class="until">——— (bis <b>31 Aug.</b>)</div>
        <div class="amount">600 €</div>
        <div class="vat">inkl. Mwst. ———————</div>
      </div>
      <div class="price-intro">
        <div class="lbl">Einführungspreis:</div>
        <div class="amount">750 €</div>
      </div>
    </div>
  </section>
  <div class="page-label" style="left:303px">Pg.1</div>

  <section class="page page--back">
    <div class="brand-tile">KERO</div>
    <div class="abs schedule-title">Workshop-Ablauf :</div>

    <div class="abs day-head" style="left:43px;top:72px;width:342px"><svg viewBox="0 0 14 13"><rect x="0.6" y="1.6" width="12.8" height="10.8" rx="1.5" fill="none" stroke="var(--wine)"/><path d="M0.6 4.6h12.8M4 0v3M10 0v3M3 7.2h8M3 9.4h5" stroke="var(--wine)"/></svg>Freitag 17-21 Uhr</div>
    <p class="abs day-copy" style="left:43px;top:92px;width:340px">Wir beginnen mit dem, wo wir gerade im Leben stehen. Wir lernen einanderkennen und erhalten Einblick in den Grundansatz von „Wachsen statt schwinden“ Wir begegnen unserer Angst und erfahren, wie wir sie fruchtbar machen können.</p>
    <ul class="abs checklist day-list" style="left:56px;top:125px">
      <li>Begrüßung</li>
      <li>Schritt 1: Im Leben sein</li>
      <li>Wieso Nachhaltigkeit nicht ausreicht und inwiefern wir mehr bewirken können</li>
      <li>Schritt 2: Die Angst durchqueren</li>
      <li>Wie wir unsere Angst fruchtbar machen</li>
      <li>Abschluss &amp; Meditation</li>
    </ul>

    <div class="abs day-head" style="left:42px;top:231px;width:208px"><svg viewBox="0 0 14 13"><rect x="0.6" y="1.6" width="12.8" height="10.8" rx="1.5" fill="none" stroke="var(--wine)"/><path d="M0.6 4.6h12.8M4 0v3M10 0v3M3 7.2h8M3 9.4h5" stroke="var(--wine)"/></svg>Samstag</div>
    <p class="abs day-copy" style="left:42px;top:251px;width:212px">Der erste Tag ist den Methoden von „Wachsen statt schwinden“ gewidmet. Eine Morgenmeditation ermöglicht uns die Begegnung mit uns selbst. Wir erforschen die zentralen Ansätze und erlernen die Kunst der Fragen, die ändern.</p>
    <p class="abs day-copy" style="left:42px;top:300px;width:212px">Wir öffnen für uns selbst Räume des Wandels und lernen, diese auch anderen Menschen zu eröffnen.</p>
    <ul class="abs checklist day-list" style="left:43px;top:326px">
      <li>Begrüßung und Morgenmeditation</li>
      <li>Schritt 3: Der Frage lauschen</li>
      <li>Die Kunst des Fragens</li>
      <li>Die sieben Schritte zur Wirksamkeit</li>
      <li>Schritt 4: In Verbindung gehen</li>
      <li>Die vier Dimensionen des Erneuerns</li>
      <li>Schritt 5: Dem Impuls lauschen</li>
      <li>Räume des Wandels schaffen</li>
      <li>Die drei Aufgaben eines Facilitators</li>
      <li>Abschluss &amp; Meditation</li>
    </ul>

    <div class="abs day-head" style="left:41px;top:479px;width:210px"><svg viewBox="0 0 14 13"><rect x="0.6" y="1.6" width="12.8" height="10.8" rx="1.5" fill="none" stroke="var(--wine)"/><path d="M0.6 4.6h12.8M4 0v3M10 0v3M3 7.2h8M3 9.4h5" stroke="var(--wine)"/></svg>Sonntag</div>
    <p class="abs day-copy" style="left:41px;top:501px;width:222px">Der zweite Tag ist uns selbst und dem Wandel gewidmet. Beide Aspekte bedingen einander. Denn Veränderung vollzieht sich nur dann, wenn wir uns selbst verändern. Wie aber kann uns das gelingen? Und wieso schützen wir uns oftmals vor Veränderungen?</p>
    <p class="abs day-copy" style="left:41px;top:550px;width:222px">Wir erkennen die Bedeutung des Anfangs und wie wir lernen, unsere Arbeit richtig zu beginnen. Zum Abschluss unterstützen uns gegenseitig, den Transfer in den Alltag zu schaffen.</p>
    <ul class="abs checklist day-list" style="left:41px;top:588px">
      <li>Begrüßung und Morgenmeditation</li>
      <li>Schritt 6: Den Anfang im Ende erkennen</li>
      <li>Schritt 7: Wirksam werden</li>
      <li>Das Zentrum: die Arbeit mit sich selbst</li>
      <li>Der Schutz vor Veränderungen: Wandel wirklich verstehen</li>
      <li>Abschluss</li>
    </ul>

    <div class="diagram-area diagram-area--steps" role="img" aria-label="Kreisdiagramm der sieben Schritte der Wirksamkeit"></div>
    <div class="diagram-title diagram-title--steps">Die sieben Schritte<br>der Wirksamkeit</div>

    <div class="diagram-title diagram-title--dims">Die Vier Dimension der<br>Erneuerung</div>
    <div class="diagram-area diagram-area--dims" role="img" aria-label="Diagramm der vier Dimensionen der Erneuerung"></div>

    <div class="abs trainer-head">Dein Trainer :</div>
    <div class="trainer-photo" role="img" aria-label="Porträtfoto des Trainers"></div>
    <div class="abs trainer-name">
      <strong>Lukas Hellwig,</strong>
      <span>Begründer von Wachsen statt schwinden.</span>
      <em>Begeisteter und inspirierender Facilitator.</em>
    </div>
  </section>
  <div class="page-label" style="left:891px">Pg.2</div>

</div>
</body>
</html>
```